Visitenkarten-Design Beratungsunternehmen
Zielgruppe
Beratung, Konzeption, Planung für medizinische Einrichtungen (Arzt- / Zahnarztpraxen)
Zielgruppe: Ärzte / Zahnärzte / Wirtschaftsberater / Planer
https://www.taleron-planwerk.de/
Aufgabenstellung
Klassische Visitenkarte zur allgemeinen Verwendung und Weitergabe.
Das Logo analog der Website, wird dann entsprechend zur Verfügung gestellt.
Kontaktdaten analog der angegebenen Website: https://www.taleron-planwerk.de/

```html
<!DOCTYPE html>
<html lang="de">
<head>
<meta charset="utf-8">
<title>Taleron Planwerk UG – Visitenkarte</title>
<link href="https://fonts.googleapis.com/css2?family=Questrial&display=swap" rel="stylesheet">
<style>
  :root {
    --bg: #d4d4d6;
    --card: #f7f7f7;
    --ink: #4b5573;
    --ink-soft: #6b748e;
    --blue: #4f6ca8;
    --green: #8dc63f;
    --rule: #8a90a4;
  }
  * { box-sizing: border-box; margin: 0; padding: 0; }
  html, body { width: 1200px; height: 900px; overflow: hidden; }
  body {
    background: var(--bg);
    font-family: "Questrial", "Century Gothic", sans-serif;
    color: var(--ink);
    position: relative;
  }
  .card {
    position: absolute;
    left: 290px;
    width: 620px;
    height: 400px;
    background: var(--card);
    box-shadow: 0 6px 18px rgba(0,0,0,0.18);
    overflow: hidden;
  }
  .card--front { top: 40px; }
  .card--back { top: 470px; }

  .edge-band {
    position: absolute;
    left: 0; right: 0; bottom: 0;
    height: 7px;
    display: flex;
  }
  .edge-band__blue { background: var(--blue); width: 40%; }
  .edge-band__gap { width: 3%; }
  .edge-band__green { background: var(--green); flex: 1; }

  /* Front */
  .brand {
    position: absolute;
    left: 50px;
    top: 150px;
    width: 200px;
    display: flex;
    align-items: flex-start;
    gap: 12px;
  }
  .brand__square {
    width: 16px; height: 16px;
    background: var(--green);
    margin-top: 8px;
    flex: none;
  }
  .brand__name {
    font-size: 27px;
    line-height: 1.05;
    color: var(--ink-soft);
  }
  .divider {
    position: absolute;
    left: 272px;
    top: 92px;
    width: 1px;
    height: 200px;
    background: var(--rule);
  }
  .contact {
    position: absolute;
    left: 300px;
    top: 82px;
    line-height: 1.2;
  }
  .contact__name { font-size: 22px; letter-spacing: 0.5px; }
  .contact__role { font-size: 14px; margin-bottom: 14px; }
  .contact__company { font-size: 17px; }
  .contact__legal { font-size: 9px; letter-spacing: 1.6px; color: var(--ink-soft); }
  .contact__address { font-size: 17px; margin-bottom: 8px; }
  .contact__line {
    display: flex;
    align-items: center;
    gap: 10px;
    font-size: 17px;
  }
  .contact__line svg { width: 14px; height: 14px; flex: none; }

  /* Back */
  .back-title {
    position: absolute;
    left: 0; right: 0;
    top: 110px;
    text-align: center;
    font-size: 54px;
    line-height: 0.95;
    color: var(--ink-soft);
  }
  .back-title__square {
    display: block;
    width: 28px; height: 28px;
    background: var(--green);
    margin: 0 auto 18px;
  }
  .services {
    position: absolute;
    left: 0; right: 0;
    bottom: 34px;
    text-align: center;
    font-size: 20px;
    letter-spacing: 2px;
    color: var(--ink);
  }
</style>
</head>
<body>

<section class="card card--front">
  <div class="brand">
    <span class="brand__square"></span>
    <span class="brand__name">Taleron<br>Planwerk UG</span>
  </div>
  <div class="divider"></div>
  <div class="contact">
    <p class="contact__name">Jonas Reimann</p>
    <p class="contact__role">Geschäftsführer</p>
    <p class="contact__company">Taleron Planwerk UG</p>
    <p class="contact__legal">(haftungsbeschränkt)</p>
    <p class="contact__address">Lindenauer Weg 12<br>04177 Leipzig</p>
    <p class="contact__line">
      <svg viewBox="0 0 16 16" aria-hidden="true"><path fill="#4b5573" d="M3.6 1.5l2.3 2.6-1.3 1.6c.9 2 2.6 3.7 4.6 4.6l1.6-1.3 2.6 2.3-1.3 2.1C7.4 13.3 2.7 8.6 1.5 3l2.1-1.5z"/></svg>
      +49 176 20481937
    </p>
    <p class="contact__line">
      <svg viewBox="0 0 16 16" aria-hidden="true"><rect x="1" y="3.5" width="14" height="9" fill="#4b5573"/><path d="M1.5 4l6.5 5 6.5-5" fill="none" stroke="#f7f7f7" stroke-width="1.2"/></svg>
      info@taleron-planwerk.de
    </p>
    <p class="contact__line">
      <svg viewBox="0 0 16 16" aria-hidden="true"><g fill="none" stroke="#4b5573" stroke-width="1.3"><circle cx="8" cy="8" r="6.3"/><ellipse cx="8" cy="8" rx="2.8" ry="6.3"/><path d="M1.7 8h12.6"/></g></svg>
      www.taleron-planwerk.de
    </p>
  </div>
  <div class="edge-band"><span class="edge-band__blue"></span><span class="edge-band__gap"></span><span class="edge-band__green"></span></div>
</section>

<section class="card card--back">
  <div class="back-title">
    <span class="back-title__square"></span>
    Taleron<br>Planwerk UG
  </div>
  <p class="services">BERATUNG | KONZEPTION | PLANUNG | UMSETZUNG</p>
  <div class="edge-band"><span class="edge-band__blue"></span><span class="edge-band__gap"></span><span class="edge-band__green"></span></div>
</section>

</body>
</html>
```